High-end construction company needs a business card design

We need a modern looking business card that draws people in, is memorable and looks so good people will want to sick it on their fridges.
On the first side what is needed are:
Logo
My name - Tomas Verbelk
Title - Managing Director
Website - www.kravel.co.uk
Email - tomas@kravel.co.uk
Telephone - 020 5194 6381
Mobile - 07845319027
On the back side was is needed is a list of all the services we provide:
-Kitchen Renovations
-Bathroom Renovations
-House Renovations
-Garage Conversions
-Extensions
-Loft Conversions
-Conservatories
-Carpentry
-Tiling
-Electrical
-Plumbing & Heating
-Bricklaying
-Landscaping
-Decorating
-Plastering
We would like the colours to be the same shades as on the logo with grey or black for the words.
Target Market(s)
Anyone who needs building work done
Contact Information for Business Card
This business card is for a construction company which strives to deliver excellent service and quality.
The look and feel of the card should represent this.
Requirements
Must have
- On the first side what is needed are:
Logo
My name - Tomas Verbelk
Title - Managing Director
Website - www.kravel.co.uk
Email - tomas@kravel.co.uk
Telephone - 020 5194 6381
Mobile - 07845319027
Nice to have
- Cool looking features

```html
<!DOCTYPE html>
<html lang="en">
<head>
<meta charset="utf-8">
<title>Kravel Construction Ltd — Business Card</title>
<link href="https://fonts.googleapis.com/css2?family=Open+Sans:wght@400;600;700&display=swap" rel="stylesheet">
<style>
  :root {
    --backdrop: #8c8c8c;
    --card: #f1f1f2;
    --green: #4caa36;
    --text: #4a4a4a;
  }
  * { margin: 0; padding: 0; box-sizing: border-box; }
  html, body {
    width: 1200px; height: 900px; overflow: hidden;
    background: var(--backdrop);
    font-family: "Open Sans", sans-serif;
    color: var(--text);
  }
  .card {
    position: absolute;
    left: 358px;
    width: 453px; height: 251px;
    background: var(--card);
  }
  .card--front { top: 163px; }
  .card--back { top: 467px; }

  .holder {
    position: absolute; right: 250px; top: 108px;
    text-align: right;
  }
  .holder__name {
    color: var(--green); font-weight: 700; font-size: 13.5px;
    letter-spacing: 0.2px; line-height: 1.1;
  }
  .holder__title { font-size: 10.5px; line-height: 1.4; }

  .divider {
    position: absolute; left: 226px; top: 98px;
    width: 1.5px; height: 56px; background: var(--green);
  }

  .contacts {
    position: absolute; left: 251px; top: 94px;
    list-style: none;
  }
  .contacts li {
    display: flex; align-items: center;
    height: 15.7px; font-size: 10.5px;
  }
  .contacts svg { width: 9px; height: 9px; margin-right: 6px; fill: var(--green); }

  .brand {
    position: absolute; left: 0; right: 0; top: 70px;
    text-align: center;
    color: var(--green); font-weight: 700;
    font-size: 19px; letter-spacing: 1.5px; line-height: 1.15;
  }

  .services {
    position: absolute; top: 161px; list-style: none;
  }
  .services--one { left: 38px; }
  .services--two { left: 185px; }
  .services--three { left: 315px; }
  .services li {
    display: flex; align-items: center;
    height: 12.6px; font-size: 10.5px;
  }
  .services li::before {
    content: ""; width: 0; height: 0; margin-right: 7px;
    border-left: 6px solid var(--green);
    border-top: 3.5px solid transparent;
    border-bottom: 3.5px solid transparent;
  }
</style>
</head>
<body>
  <section class="card card--front">
    <div class="holder">
      <div class="holder__name">TOMAS VERBELK</div>
      <div class="holder__title">Managing Director</div>
    </div>
    <div class="divider"></div>
    <ul class="contacts">
      <li><svg viewBox="0 0 10 10"><path d="M2 0.5 L3.5 2.8 L2.6 3.8 Q3.6 6 6 7.3 L7 6.3 L9.5 7.8 L8.3 9.5 Q4 9 1.2 5 Q0 2.5 2 0.5Z"/></svg>020 5194 6381</li>
      <li><svg viewBox="0 0 10 10"><path d="M2.5 0h5v10h-5z M3.4 1v7h3.2V1z"/></svg>07845319027</li>
      <li><svg viewBox="0 0 10 10"><path d="M0 2h10v6H0z M0.8 2.6 5 5.6 9.2 2.6z" fill-rule="evenodd"/></svg>tomas@kravel.co.uk</li>
      <li><svg viewBox="0 0 10 10"><circle cx="5" cy="5" r="4.5"/></svg>www.kravel.co.uk</li>
    </ul>
  </section>

  <section class="card card--back">
    <div class="brand">KRAVEL<br>CONSTRUCTION LTD</div>
    <ul class="services services--one">
      <li>Kitchen Renovations</li>
      <li>Bathroom Renovations</li>
      <li>House Renovations</li>
      <li>Garage Conversions</li>
      <li>Extensions</li>
    </ul>
    <ul class="services services--two">
      <li>Plumbing &amp; Heating</li>
      <li>Bricklaying</li>
      <li>Landscaping</li>
      <li>Decorating</li>
      <li>Plastering</li>
    </ul>
    <ul class="services services--three">
      <li>Loft Conversions</li>
      <li>Conservatories</li>
      <li>Carpentry</li>
      <li>Tiling</li>
      <li>Electrical</li>
    </ul>
  </section>
</body>
</html>
```